Luxury Green Baseline/academy - Webdesign

We want to develop a cutting edge website for a luxury tennis academy. Academy is based in Russia and includes all the necessary amenities for comfortable stay: apartments, spa, tennis courts, training facilities, etc.
We would like to see a clean, simple and modern design (with implementation of all the current trends in web design, although our project has to be distinct and unique).
Color scheme: we would like to see colors present in our logos and all the current associated with tennis. We are open to your ideas and creativity on this front.
The final design should communicate simplicity, be user friendly and convey premium feel.
We woud like to see unique ideas in the design, unconventional techniques, etc.
We don't want standard template design!
Updates
We want to mention that this Tennis Academy has a light focus on nature, as the new material we have uploaded illustrates.
Additional comment to everyone!
We couldn't upload this file to the system: it is too big.
Thank you everyone for your submissions!
Industry/Entity Type
Training
Requirements
Must have
- We would like to see the designs for the following pages:
Home Page:
- Slideshow
- Short description and all the standard stuff
About Us:
- Description with some images
Services:
- Simple description of all of the provided services and possibility to book all of them on the website
! Important ! Develop small system for booking of the days of stay and registration for the courses
Booking and registration !
News:
- Creative layout to display recent news of the academy
Coaches:
- Image and short description of our staff.
Club / Gallery:
- Images and descriptions of the amenities in the territory.
We want a unique display of images: not just lines and rows filled with images
- One idea: an interactive map that displays images and description on mouseover or click on the object on the map (but again, we are open to all your ideas)
Contacts:
- Contact form, contacts, etc.
Sport Store:
- Basic layout for the goods and services provided by the sports store located in the academy
Prices:
- Price lists and ranges with a button leading to registration and booking
For pages like About Us and Services, it would be enough to develop one unified layout for all of them.

```html
<!DOCTYPE html>
<html lang="en">
<head>
<meta charset="utf-8">
<title>Green Baseline – Home</title>
<link href="https://fonts.googleapis.com/css2?family=Ubuntu:ital,wght@0,300;0,400;0,500;1,300;1,400&display=swap" rel="stylesheet">
<style>
  :root {
    --green-dark: #1f7a3a;
    --green: #2e8b3e;
    --green-mid: #4a9a3c;
    --lime: #d6e21c;
    --lime-deep: #3fa33a;
    --yellow: #f2e51a;
    --panel: rgba(28, 30, 30, 0.78);
    --panel-line: rgba(255, 255, 255, 0.12);
    --field: rgba(10, 10, 10, 0.75);
    --text-dark: #3a3a3a;
    --text-soft: #5a5a5a;
    --white: #ffffff;
    --footer-text: #8a8a8a;
  }
  * { margin: 0; padding: 0; box-sizing: border-box; }
  html, body { width: 1200px; height: 750px; overflow: hidden; background: var(--white); }
  body { font-family: "Ubuntu", sans-serif; position: relative; }

  .hero {
    position: absolute; left: 0; top: 0; width: 1200px; height: 632px;
    background:
      radial-gradient(ellipse at 85% 10%, rgba(255,255,255,0.95) 0%, rgba(255,255,255,0) 45%),
      linear-gradient(180deg, #b9c9cf 0%, #dfe6e4 30%, #e9ecea 48%, #9ba59e 62%, #6e5a4c 78%, #5d3f33 100%);
  }
  .hero-border { position: absolute; left: 0; top: 632px; width: 1200px; height: 2px; background: var(--green); }

  .brand {
    position: absolute; left: 44px; top: 38px;
    display: flex; align-items: center; gap: 8px;
    font-size: 30px; font-weight: 500; color: var(--green);
  }
  .brand-dot { width: 26px; height: 26px; border-radius: 50%; background: var(--lime-deep); }

  .sidebar {
    position: absolute; left: 44px; top: 126px; width: 180px; height: 470px;
    background: var(--panel); border-radius: 4px;
    border: 1px solid rgba(255,255,255,0.08);
  }
  .nav { list-style: none; padding: 15px 11px 0 11px; }
  .nav li {
    height: 33px; line-height: 31px; padding-left: 12px;
    font-size: 13px; font-style: italic; font-weight: 300; color: var(--white);
    border-bottom: 1px solid var(--panel-line);
  }
  .nav li:last-child { border-bottom: none; }
  .nav li.is-active {
    color: #1c2a10; font-weight: 400; padding-left: 18px; margin-right: -2px;
    background: linear-gradient(90deg, var(--lime) 0%, var(--lime-deep) 100%);
    clip-path: polygon(0 0, 94% 0, 100% 50%, 94% 100%, 0 100%);
    border-radius: 3px 0 0 3px; border-bottom: none; margin-bottom: 1px; line-height: 30px; height: 31px;
  }
  .booking { position: absolute; left: 12px; top: 338px; width: 152px; }
  .booking-title { font-size: 18px; font-style: italic; font-weight: 300; color: var(--yellow); margin-bottom: 10px; padding-left: 10px; }
  .field {
    height: 24px; background: var(--field); border-radius: 3px; margin-bottom: 7px;
    font-size: 9px; font-style: italic; color: #9a9a9a; padding-left: 17px; line-height: 24px;
    display: flex; justify-content: space-between; align-items: center;
  }
  .field-btn {
    height: 18px; line-height: 18px; padding: 0 6px; margin-right: 3px;
    background: #3a3a3a; color: var(--white); font-style: normal; font-size: 8px; border-radius: 2px;
  }

  .btn-arrow {
    position: absolute; display: flex; align-items: center; justify-content: center;
    background: linear-gradient(90deg, var(--lime) 0%, var(--lime-deep) 100%);
    clip-path: polygon(0 0, 92% 0, 100% 50%, 92% 100%, 0 100%);
    border-radius: 4px 0 0 4px;
    color: #1c2a10; font-style: italic; font-size: 12px;
  }
  .btn-book { left: 122px; top: 560px; width: 84px; height: 22px; font-size: 11px; }
  .btn-read { left: 254px; top: 355px; width: 118px; height: 27px; }

  .intro { position: absolute; left: 254px; top: 136px; width: 282px; }
  .intro-kicker { font-size: 31px; font-weight: 300; color: var(--green-mid); line-height: 38px; white-space: nowrap; }
  .intro-title { font-size: 42px; font-weight: 300; color: var(--green-dark); line-height: 46px; margin-bottom: 14px; white-space: nowrap; }
  .intro-lead { font-size: 11px; font-style: italic; font-weight: 300; color: var(--text-dark); line-height: 14px; margin-bottom: 11px; }
  .intro-body { font-size: 9px; font-weight: 300; color: var(--text-soft); line-height: 13.5px; }

  .news { position: absolute; left: 797px; top: 198px; width: 360px; }
  .news-heading { font-size: 18px; font-weight: 300; color: var(--green-dark); margin-bottom: 18px; }
  .news-item { display: flex; gap: 19px; }
  .news-thumb { width: 57px; height: 57px; flex: none; margin-top: -6px; background: rgba(255,255,255,0.85); }
  .news-title { font-size: 11px; font-weight: 300; color: var(--green-mid); margin-bottom: 2px; }
  .news-text { font-size: 9px; font-weight: 300; color: var(--text-dark); line-height: 13px; }
  .news-more { font-size: 8px; font-style: italic; color: var(--green); margin-top: 2px; }

  .slider-arrow { position: absolute; top: 527px; }
  .slider-prev { left: 1028px; }
  .slider-next { left: 1132px; }

  .scroll-down { position: absolute; left: 585px; top: 617px; }

  .footer {
    position: absolute; left: 0; top: 682px; width: 1200px; text-align: center;
    font-size: 9px; font-weight: 300; color: var(--footer-text);
  }
  .footer span { color: var(--green); }
</style>
</head>
<body>
  <div class="hero" role="img" aria-label="Photo of a tennis player in a black top and white skirt standing at a court fence, with clay courts, an air dome and club houses under a bright cloudy sky"></div>
  <div class="hero-border"></div>

  <div class="brand"><span>Green Baseline</span><span class="brand-dot"></span></div>

  <aside class="sidebar">
    <ul class="nav">
      <li>About us</li>
      <li>Services</li>
      <li class="is-active">Booking &amp; Registration</li>
      <li>News</li>
      <li>Coaches</li>
      <li>Club Gallery</li>
      <li>Contacts</li>
      <li>Sport Store</li>
      <li>Prices</li>
    </ul>
    <div class="booking">
      <div class="booking-title">Booking</div>
      <div class="field">Your name here</div>
      <div class="field">Date you want to book <span class="field-btn">select</span></div>
    </div>
  </aside>
  <div class="btn-arrow btn-book">Book Me!</div>

  <section class="intro">
    <div class="intro-kicker">Welcome on</div>
    <h1 class="intro-title">Green Baseline!</h1>
    <p class="intro-lead">Lorem ipsum dolor sit amet, consectetur adipiscing elit. Etiam ut nibh dolor. Vivamus ac lacus ipsum, a pretium magna.</p>
    <p class="intro-body">Integer porttitor lorem eu orci dictum pharetra. Suspendisse diam nisi, malesuada vel faucibus id, pretium eget nulla. Nulla iaculis, magna a feugiat dapibus, odio magna auctor dui, eu suscipit velit urna scelerisque purus. In pharetra feugiat massa ac tincidunt. In hac habitasse platea dictumst.</p>
  </section>
  <div class="btn-arrow btn-read">Read More</div>

  <section class="news">
    <h2 class="news-heading">What’s new?</h2>
    <div class="news-item">
      <div class="news-thumb"></div>
      <div>
        <div class="news-title">Suspendisse ac lorem fermentum</div>
        <div class="news-text">metus commodo consequat ac in velit. Aliquam iaculis consectetur aliquet. Vestibulum semper interdum massa, nec semper velit faucibus in.</div>
        <div class="news-more">read more &gt;&gt;</div>
      </div>
    </div>
  </section>

  <svg class="slider-arrow slider-prev" width="32" height="50" viewBox="0 0 32 50" aria-hidden="true">
    <polyline points="28,3 5,25 28,47" fill="none" stroke="rgba(255,255,255,0.45)" stroke-width="4"/>
  </svg>
  <svg class="slider-arrow slider-next" width="32" height="50" viewBox="0 0 32 50" aria-hidden="true">
    <polyline points="4,3 27,25 4,47" fill="none" stroke="rgba(255,255,255,0.45)" stroke-width="4"/>
  </svg>

  <svg class="scroll-down" width="30" height="30" viewBox="0 0 30 30" aria-hidden="true">
    <circle cx="15" cy="15" r="14" fill="#ffffff" stroke="#2e8b3e" stroke-width="2"/>
    <circle cx="15" cy="15" r="10" fill="#3fa33a"/>
    <path d="M15 9 V20 M10.5 15.5 L15 20 L19.5 15.5" fill="none" stroke="#ffffff" stroke-width="2.2" stroke-linecap="round" stroke-linejoin="round"/>
  </svg>

  <footer class="footer">Copyright 2012 © <span>Green Baseline</span>. All Rights Reserved.</footer>
</body>
</html>
```